Bright Parcel is a blog featuring products that give back. Products with a conscience.

The style of the blog should be STYLISH, Clean CHIC lines.
Color's to be used Grey & yellow or
Grey & navy blue.

examples/style references:

http://pantryloft.example/provisions (this one is my favorite)

http://mindfulvane.example/portfolio/commerce-home-facelift/

http://www.korvadine.example

Attached are style references as a guidelines.

It is time to create an alternative form of raising cash for good, other than traditional fundraising.

You proceeds go towards "Project based" causes. For example- helping feed children a lunch meal via the Tiffinrow fund.

The blog will feature-Special Limited Edition partnerships/collaborations with brands like ZUT will donate 100 percent of the proceeds to specific charities.

There will be a social component- where sharing it on your social media is essential. For example- I can post my purchase of jeans from Marrow on my Chatterly and the cause I helped. "Check out my new jeans & it's super amazing that I fed a child a lunch meal at the same time". Nominate your friends to do the same.

```html
<!DOCTYPE html>
<html lang="en">
<head>
<meta charset="utf-8">
<title>Bright Parcel</title>
<link rel="stylesheet" href="https://fonts.googleapis.com/css2?family=Questrial&family=Droid+Serif:ital@0;1&family=Cabin:wght@400;500&family=Noticia+Text:ital@1&display=swap">
<style>
  :root {
    --page: #e9e9e9;
    --band: #b1cadf;
    --band-line: #d6e3ee;
    --ink: #3a3a3a;
    --ink-soft: #555555;
    --band-ink: #4a5763;
    --frame: #ffffff;
    --rule: #dcdcdc;
  }
  * { box-sizing: border-box; margin: 0; padding: 0; }
  html, body { width: 810px; height: 1200px; overflow: hidden; }
  body {
    position: relative;
    background: var(--page);
    color: var(--ink);
    font-family: "Cabin", sans-serif;
  }
  .abs { position: absolute; }

  /* header */
  .brand {
    left: 153px; top: 46px;
    font-family: "Questrial", sans-serif;
    font-size: 22px; letter-spacing: 2px;
    color: #222;
    text-transform: uppercase;
  }
  .nav { left: 466px; top: 40px; display: flex; gap: 18px; list-style: none; }
  .nav li { font-family: "Cabin", sans-serif; font-size: 7.5px; color: #333; letter-spacing: .3px; }
  .search {
    left: 552px; top: 66px; width: 112px; height: 16px;
    background: #fff; border: 1px solid #cfcfcf; display: flex;
  }
  .search span { flex: 1; font-family: "Droid Serif", serif; font-size: 7.5px; font-weight: bold; color: #555; padding: 3px 4px; }
  .search i { width: 14px; border-left: 1px solid #ddd; display: flex; align-items: center; justify-content: center; }

  /* bands */
  .band {
    left: 146px; width: 518px; height: 38px;
    background: var(--band);
    border-top: 2px solid var(--band-line);
    box-shadow: 0 -3px 0 -1px var(--band);
    display: flex; align-items: center; justify-content: center;
    font-family: "Noticia Text", "Droid Serif", serif; font-style: italic;
    color: var(--band-ink);
  }
  .band--intro { top: 108px; font-size: 14.5px; }
  .band--product { top: 486px; font-size: 15px; }
  .intro {
    left: 158px; top: 158px; width: 494px; text-align: center;
    font-family: "Droid Serif", serif; font-style: italic; font-size: 7.5px; line-height: 13px;
    color: var(--ink-soft);
  }

  /* slider */
  .slider {
    left: 145px; top: 206px; width: 519px; height: 160px;
    background: var(--frame); padding: 4px;
    box-shadow: 0 10px 10px -8px rgba(0,0,0,.25);
  }
  .slider .photo { width: 100%; height: 100%; background: linear-gradient(180deg, #73919c 0%, #6a8994 70%, #9aa9a8 100%); }
  .arrow {
    width: 15px; height: 15px; border-radius: 50%; background: #fff;
    border: 1px solid #cfcfcf; display: flex; align-items: center; justify-content: center; top: 271px;
  }
  .arrow--prev { left: 138px; }
  .arrow--next { left: 653px; }
  .dots { left: 388px; top: 380px; display: flex; gap: 4px; }
  .dots span { width: 9px; height: 9px; border-radius: 50%; background: #f4f4f4; border: 1px solid #cfcfcf; }
  .dots span.on { background: #bdbdbd; }

  /* features */
  .feature { top: 404px; width: 226px; }
  .feature h3, .product h3 { font-family: "Cabin", sans-serif; font-weight: 400; font-size: 10.5px; color: #333; margin-bottom: 8px; }
  .feature p, .product p { font-size: 6.3px; line-height: 10.5px; color: #333; }

  /* products */
  .product { width: 165px; }
  .product .thumb {
    width: 165px; height: 107px; background: var(--frame); padding: 4px;
    box-shadow: 0 9px 8px -7px rgba(0,0,0,.28);
  }
  .product .thumb div { width: 100%; height: 100%; }
  .product h3 { margin-top: 20px; margin-bottom: 6px; }
  .product h3 em { font-style: normal; margin-left: 10px; }

  /* footer */
  .footer-band {
    left: 145px; top: 944px; width: 520px; height: 36px; background: var(--band);
    font-size: 7px; font-weight: 500; color: #3c4750;
  }
  .footer-band span { position: absolute; top: 15px; }
  .footer-text { left: 149px; top: 994px; width: 205px; font-size: 6.5px; line-height: 11px; color: #333; }
  .footer-text p + p { margin-top: 10px; }
  .contact { left: 385px; top: 994px; list-style: none; font-size: 6.5px; color: #333; }
  .contact li { margin-bottom: 7px; }
  .contact b { font-weight: 400; display: inline-block; width: 14px; }
  .social { left: 537px; top: 997px; display: flex; gap: 6px; }
  .social span {
    width: 19px; height: 19px; border-radius: 50%;
    background: radial-gradient(circle at 50% 35%, #fafafa, #d8d8d8);
    border: 1px solid #c6c6c6;
  }
  .bottom-rule { left: 145px; top: 1144px; width: 519px; height: 1px; background: var(--rule); }
</style>
</head>
<body>
  <header>
    <div class="abs brand">Bright Parcel</div>
    <ul class="abs nav">
      <li>HOME</li><li>PRODUCT</li><li>SERVICES</li><li>ABOUT</li><li>CONTACT</li>
    </ul>
    <div class="abs search">
      <span>Search</span>
      <i><svg width="8" height="8" viewBox="0 0 8 8"><circle cx="3.3" cy="3.3" r="2.4" fill="none" stroke="#aaa" stroke-width="1"/><line x1="5" y1="5" x2="7.5" y2="7.5" stroke="#aaa" stroke-width="1"/></svg></i>
    </div>
  </header>

  <section>
    <h1 class="abs band band--intro">Lorem ipsum dolor si amet enim elit lectus felis, malesuada ultricies</h1>
    <p class="abs intro">Vestibulum commodo volutpat a, convallis ac, laoreet enim. Phasellus fermentum in, dolor. Pellentesque facilisis. Nulla imperdiet sit amet magna. Vestibulum dapibus, mauris nec malesuada fames ac turpis velit, rhoncus eu, luctus et interdum adipiscing wisi.</p>

    <div class="abs slider"><div class="photo" role="img" aria-label="Kitchen shelf with aprons, a twine spool, flowers in a vase and metal canisters against a blue-grey wall"></div></div>
    <div class="abs arrow arrow--prev"><svg width="6" height="7" viewBox="0 0 6 7"><path d="M4.5 0.5 1.5 3.5 4.5 6.5" fill="none" stroke="#333" stroke-width="1.4"/></svg></div>
    <div class="abs arrow arrow--next"><svg width="6" height="7" viewBox="0 0 6 7"><path d="M1.5 0.5 4.5 3.5 1.5 6.5" fill="none" stroke="#333" stroke-width="1.4"/></svg></div>
    <div class="abs dots"><span></span><span></span><span class="on"></span></div>

    <article class="abs feature" style="left:145px">
      <h3>Aliquam erat ac ipsum</h3>
      <p>Lorem ipsum dolor sit amet enim. Etiam ullamcorper. Suspendisse a pellentesque dui, non felis. Maecenas malesuada elit lectus felis, malesuada ultricies. Curabitur et ligula. Ut molestie a, ultricies porta urna. / ... /</p>
    </article>
    <article class="abs feature" style="left:443px">
      <h3>Pellentesque facilisis</h3>
      <p>Lorem ipsum dolor sit amet enim. Etiam ullamcorper. Suspendisse a pellentesque dui, non felis. Maecenas malesuada elit lectus felis, malesuada ultricies. Curabitur et ligula. Ut molestie a, ultricies porta urna. / ... /</p>
    </article>
  </section>

  <section>
    <h2 class="abs band band--product">Product</h2>

    <article class="abs product" style="left:145px;top:545px">
      <div class="thumb"><div role="img" aria-label="Two woven baskets on white planks" style="background:linear-gradient(135deg,#cfd6dc,#a89275)"></div></div>
      <h3>Aliquam erat ac ipsum <em>$75</em></h3>
      <p>Lorem ipsum dolor sit amet enim. Etiam ullamcorper. Suspendisse a pellentesque dui, non felis.</p>
    </article>
    <article class="abs product" style="left:322px;top:545px">
      <div class="thumb"><div role="img" aria-label="Stoneware jug beside a glass of whisky" style="background:linear-gradient(180deg,#8fa5b2,#c9c3b6)"></div></div>
      <h3>Pellentesque facilisis <em>$60</em></h3>
      <p>Lorem ipsum dolor sit amet enim. Etiam ullamcorper. Suspendisse a pellentesque dui, non felis.</p>
    </article>
    <article class="abs product" style="left:499px;top:545px">
      <div class="thumb"><div role="img" aria-label="Wooden bowl of limes on a table" style="background:linear-gradient(180deg,#a9c2c6,#b58a5c 75%,#d8d8d8)"></div></div>
      <h3 style="margin-top:20px;margin-bottom:0">Lorem ipsum <em>$45</em></h3>
      <p>Lorem ipsum dolor sit amet enim. Etiam ullamcorper. Suspendisse a pellentesque dui, non felis.</p>
    </article>

    <article class="abs product" style="left:145px;top:742px">
      <div class="thumb"><div role="img" aria-label="Set of stainless steel canisters" style="background:linear-gradient(180deg,#b9cdd6,#8c9aa3 60%,#d7e1e6)"></div></div>
      <h3>Aliquam erat ac ipsum <em>$75</em></h3>
      <p>Lorem ipsum dolor sit amet enim. Etiam ullamcorper. Suspendisse a pellentesque dui, non felis.</p>
    </article>
    <article class="abs product" style="left:322px;top:742px">
      <div class="thumb"><div role="img" aria-label="White anemones in a low dish" style="background:linear-gradient(180deg,#8ea2ab,#e6e7e6 55%,#a9b2b6)"></div></div>
      <h3>Pellentesque facilisis <em>$60</em></h3>
      <p>Lorem ipsum dolor sit amet enim. Etiam ullamcorper. Suspendisse a pellentesque dui, non felis.</p>
    </article>
    <article class="abs product" style="left:499px;top:742px">
      <div class="thumb"><div role="img" aria-label="Cup of coffee on a white tray with sweets" style="background:linear-gradient(135deg,#9aa6aa,#e6e4df 60%,#8b8f90)"></div></div>
      <h3>Lorem ipsum <em>$45</em></h3>
      <p>Lorem ipsum dolor sit amet enim. Etiam ullamcorper. Suspendisse a pellentesque dui, non felis.</p>
    </article>
  </section>

  <footer>
    <div class="abs footer-band">
      <span style="left:5px;top:14px">Quisque lorem</span>
      <span style="left:256px;top:17px">Contact Us</span>
      <span style="left:392px;top:17px">Get Social</span>
    </div>
    <div class="abs footer-text">
      <p>Lorem ipsum dolor sit amet enim. Etiam ullamcorper. Suspendisse a pellentesque dui, non felis. Maecenas malesuada elit lectus felis, malesuada ultricies.</p>
      <p>Curabitur et ligula. Ut molestie a, ultricies porta urna. Vestibulum commodo volutpat a, convallis ac, laoreet enim.</p>
      <p>Phasellus fermentum in, dolor. Pellentesque facilisis. Nulla imperdiet sit amet magna.</p>
    </div>
    <ul class="abs contact">
      <li><b>P:</b> +44 55500 000 000</li>
      <li><b>E:</b> hello@brightparcel.example</li>
      <li><b>W:</b> www.brightparcel.example</li>
      <li><b>A:</b> Lorem, Ipsum, Dolor 10</li>
    </ul>
    <div class="abs social" aria-label="Social links">
      <span></span><span></span><span></span><span></span><span></span>
    </div>
    <div class="abs bottom-rule"></div>
  </footer>
</body>
</html>
```